Verpackungsdesign für hochwertiges Kaninchenfutter
Zielgruppe
Wir bieten hochwertiges Futter (Hauptfutter wie Heu aus eigener Herstellung aber auch Zusatzfutter) für Kaninchen.
Unsere Zielgruppe sind laut Auswertung unsers Online-Shops hauptsächlich weibliche Kunden (82%) und im Durchschnitt 40 Jahre alt.
Hallo,
es geht um eine gesamte Druckvorlage für durchsichtige LDPE-Beutel. Es sollte daher ein Layout sein, bei dem das Logo abgesetzt sozusagen separat überhalb des anderen sich darstellt.
Das Layout sollte insgesamt 5500mm breit und ca. 400mm hoch sein. Der gesamte Beutel hat das Maß von 550x900mm (liegend)
Bitte die angefügten Bilder und den Layoutentwurf berücksichtigen.
Hierbei müssen nicht alle Bilder oder Texte verwendet werden, bzw es können gerne andere Layoutbilder benutzt werden.
Als Referenzbeispiele sind 3 Layouts von Mitbewerbern angefügt, die wir sehr gut finden.

```html
<!DOCTYPE html>
<html lang="de">
<head>
<meta charset="utf-8">
<title>Heufreund – Beutel-Etikett</title>
<link href="https://fonts.googleapis.com/css2?family=Dosis:wght@400;500;600;700&family=Lato:wght@400;700&display=swap" rel="stylesheet">
<style>
:root{
  --lime:#b3cc2b;
  --lime-light:#c6db4a;
  --forest:#1d6236;
  --forest-dark:#17532d;
  --ink:#ffffff;
  --blue:#1f5f93;
  --field-top:#cfe0a0;
  --field-mid:#a9bf52;
  --field-low:#d8c667;
  --bg:#f4f4f0;
}
*{margin:0;padding:0;box-sizing:border-box}
html,body{width:1200px;height:1200px;overflow:hidden;background:var(--bg)}
body{position:relative;font-family:"Dosis",sans-serif;color:var(--ink)}

/* ---------- Oberes Logo-Etikett ---------- */
.brand-label{position:absolute;left:300px;top:110px;width:600px;height:290px}
.brand-band{position:absolute;left:0;top:70px;width:600px;height:220px;background:var(--lime)}
.brand-seal{position:absolute;left:160px;top:0;width:170px;height:170px;border-radius:50%;background:#fff;
  display:flex;align-items:center;justify-content:center}
.brand-seal span{font-family:"Dosis",sans-serif;font-weight:700;font-size:28px;color:var(--forest)}
.brand-claim{position:absolute;left:32px;top:186px;font-size:22px;font-weight:500;letter-spacing:.5px;text-transform:uppercase}
.brand-url{position:absolute;left:32px;top:218px;font-size:36px;font-weight:600;letter-spacing:1.5px;text-transform:uppercase}
.tradition-badge{position:absolute;left:470px;top:165px;width:112px;height:112px;border-radius:50%;background:var(--forest)}

/* ---------- Unteres Info-Etikett ---------- */
.info-label{position:absolute;left:130px;top:470px;width:940px;height:640px;overflow:hidden;
  background:linear-gradient(180deg,var(--field-top) 0%,var(--field-mid) 35%,var(--field-low) 70%,#cfd46a 100%)}
.landscape{position:absolute;inset:0}
.mascot{position:absolute;left:150px;top:40px;width:120px;height:150px;border-radius:40% 40% 45% 45%;background:#a56a3c;opacity:.85}
.quality-badge{position:absolute;left:15px;top:200px;width:150px;height:150px;border-radius:50%;background:var(--forest);opacity:.9}
.handpacked{position:absolute;left:720px;top:220px;width:130px;height:90px;border-radius:14px;background:var(--lime-light)}
.bale{position:absolute;left:580px;top:340px;width:300px;height:300px;border-radius:50%;
  background:radial-gradient(circle,#c2b267 0%,#a99a4c 60%,#8f8240 100%)}

.content-box{position:absolute;left:275px;top:135px;width:350px}
.content-head{background:var(--forest);padding:12px 14px;font-size:24px;font-weight:500;line-height:1.15;text-align:center;text-transform:uppercase}
.content-list{background:var(--lime);padding:12px 22px;list-style:none}
.content-list li{display:flex;align-items:center;gap:14px;font-size:22px;line-height:1.35}
.content-list li::before{content:"";width:20px;height:20px;border:2px solid #fff;border-radius:50%;flex:none}
.content-foot{background:var(--forest);padding:10px 14px;font-size:22px;line-height:1.2;text-align:center}

.contact{position:absolute;left:40px;top:425px;font-family:"Lato",sans-serif;font-size:10px;line-height:1.35;color:#fff}
.rating-badge{position:absolute;left:200px;top:425px;width:72px;height:72px;border-radius:6px;background:#fff}

.benefits{position:absolute;left:300px;top:490px;list-style:none;font-size:14px;font-weight:500;line-height:1.3;text-transform:uppercase}
.benefits li::before{content:"• "}

.info-tag{position:absolute;display:flex;align-items:center;gap:12px;background:var(--blue);
  font-family:"Lato",sans-serif;font-weight:700;font-size:14px;line-height:1.25;padding:10px 16px}
.info-tag svg{flex:none}
.tag-tested{left:25px;top:530px;width:250px}
.tag-family{left:640px;top:560px;width:270px}
</style>
</head>
<body>

<section class="brand-label">
  <div class="brand-band"></div>
  <div class="brand-seal"><span>Heufreund</span></div>
  <p class="brand-claim">Gesundes Futter für gesunde Tiere</p>
  <p class="brand-url">heufreund-shop.de</p>
  <div class="tradition-badge" role="img" aria-label="Rundes Siegel: Qualität aus Tradition"></div>
</section>

<section class="info-label">
  <div class="landscape" role="img" aria-label="Sommerliche Hügellandschaft der Eifel mit Feldern und Heuballen"></div>
  <div class="mascot" role="img" aria-label="Gezeichnetes Kaninchen-Maskottchen"></div>
  <div class="quality-badge" role="img" aria-label="Handgeschriebenes Siegel: 100% Qualität natürlich"></div>
  <div class="handpacked" role="img" aria-label="Handschrift-Schild: Handverpackt!"></div>
  <div class="bale" role="img" aria-label="Rundballen Heu mit zwei Kaninchen davor"></div>

  <div class="content-box">
    <p class="content-head">In diesem frisch verpackten Päckchen findest du:</p>
    <ul class="content-list">
      <li>4 kg Qualitäts-Heu</li>
      <li>4 kg Premium-Heu</li>
      <li>3 kg Qualitäts-Stroh</li>
    </ul>
    <p class="content-foot">…aus unserer günen Eifel<br>für dein LIEBLINGSTIER!</p>
  </div>

  <address class="contact">
    HEUFREUND.DE<br>Inhaber: K. Brandt<br>Wiesenweg 12<br>54321 Talheim (Eifel)<br>info@heufreund-shop.de<br>www.heufreund-shop.de
  </address>
  <div class="rating-badge" role="img" aria-label="Bewertungssiegel"></div>

  <ul class="benefits">
    <li>Hoher Rohfasergehalt</li>
    <li>Frischer &amp; aromatischer Heuduft</li>
    <li>Optimale Versorgung durch Nähr- und Ballaststoffe</li>
    <li>Grobe &amp; lange Struktur für gute Zahnpflege</li>
    <li>Ernteschonende Trocknung</li>
  </ul>

  <div class="info-tag tag-tested">
    <svg width="34" height="34" viewBox="0 0 34 34" fill="none" stroke="#fff" stroke-width="2">
      <circle cx="17" cy="14" r="10"/><path d="M11 22 L9 32 L17 28 L25 32 L23 22"/><path d="M12 14 l4 4 l7 -7"/>
    </svg>
    <span>Geprüftes Qualitätsheu<br>aus der Eifel</span>
  </div>

  <div class="info-tag tag-family">
    <svg width="38" height="34" viewBox="0 0 38 34" fill="none" stroke="#fff" stroke-width="2">
      <path d="M3 16 L19 3 L35 16"/><path d="M7 13 V31 H31 V13"/><path d="M15 31 V21 H23 V31"/>
    </svg>
    <span>Familienbetrieb seit<br>über 100 Jahren</span>
  </div>
</section>

</body>
</html>
```